Personal Blog

The wordpress blog style and layout should be similar to http://www.danholtmere.com

homepage: my photo, list of things, call to action then 3 boxes (The Blog, The Book and podcast)

Other pages: About us, Blog, Consulting, Contact

Target Market(s)

Web Marketing Consultant

Industry/Entity Type

Consulting

Colors
3277b5
33a6d7
f04a50
f68e4e
33b7a4

```html
<!DOCTYPE html>
<html lang="en">
<head>
<meta charset="utf-8">
<title>Business Bootcamp</title>
<link href="https://fonts.googleapis.com/css2?family=Arimo:wght@400;700&family=Open+Sans:wght@400;600;700&display=swap" rel="stylesheet">
<style>
  :root {
    --red: #f04a50;
    --ink: #333333;
    --text: #555555;
    --muted: #777777;
    --page: #ececec;
    --panel: #f1f1f1;
    --card: #f8f8f8;
    --card-head: #888888;
    --line: #d9d9d9;
    --blue: #33a6d7;
    --white: #ffffff;
  }
  * { margin: 0; padding: 0; box-sizing: border-box; }
  html, body { width: 1200px; height: 1000px; overflow: hidden; }
  body {
    position: relative;
    background: var(--page);
    font-family: "Arimo", Arial, sans-serif;
    color: var(--text);
  }

  .site-header {
    position: absolute; left: 0; top: 0; width: 1200px; height: 79px;
    background: var(--white); border-bottom: 4px solid #e4e4e4;
  }
  .brand {
    position: absolute; left: 235px; top: 23px;
    font-family: "Open Sans", sans-serif; font-weight: 600; font-size: 21px;
    color: var(--ink); letter-spacing: 0.3px;
  }
  .main-nav a {
    position: absolute; top: 30px; font-size: 11px; font-weight: 700;
    color: var(--text); text-decoration: none;
  }

  .hero-title {
    position: absolute; left: 0; width: 1232px; top: 135px; text-align: center;
    font-size: 24.4px; font-weight: 700; color: var(--text);
  }
  .hero-title em { font-style: normal; color: var(--red); }
  .hero-sub {
    position: absolute; left: 0; width: 1232px; top: 170px; text-align: center;
    font-size: 13.5px; font-weight: 700; color: #666;
  }

  .portrait {
    position: absolute; left: 335px; top: 220px; width: 205px; height: 262px;
    background: linear-gradient(180deg, #d8d3cf 0%, #8a8c90 35%, #5c5f63 70%, #4a4c50 100%);
    border-radius: 90px 90px 0 0;
  }

  .benefits { position: absolute; left: 565px; top: 299px; list-style: none; }
  .benefits li {
    display: flex; align-items: center; height: 21.4px;
    font-size: 10.7px; color: #444;
  }
  .benefits svg { width: 14px; height: 12px; margin-right: 9px; }

  .cta-bar {
    position: absolute; left: 235px; top: 483px; width: 762px; height: 86px;
    background: var(--panel); border: 1px solid var(--line);
  }
  .cta-title { position: absolute; left: 31px; top: 20px; font-size: 11.4px; font-weight: 700; color: #666; }
  .cta-text { position: absolute; left: 31px; top: 37px; width: 540px; font-size: 9.3px; line-height: 15px; color: #666; }
  .cta-divider { position: absolute; left: 580px; top: 22px; width: 1px; height: 40px; background: #dcdcdc; }
  .cta-button {
    position: absolute; left: 607px; top: 22px; width: 129px; height: 38px;
    background: var(--red); color: var(--white); font-weight: 700; font-size: 14px;
    display: flex; align-items: center; justify-content: center; text-decoration: none;
  }

  .features {
    position: absolute; left: 235px; top: 590px; width: 762px; height: 300px;
    background: var(--panel); border: 1px solid var(--line);
  }
  .feature {
    position: absolute; top: 24px; width: 225px; height: 250px; background: var(--card);
  }
  .feature-head {
    height: 40px; background: var(--card-head); color: var(--white);
    font-family: "Open Sans", sans-serif; font-weight: 600; font-size: 13px;
    display: flex; align-items: center; justify-content: center;
  }
  .feature-text { position: absolute; left: 18px; top: 61px; width: 186px; font-size: 10.4px; line-height: 14px; color: var(--muted); }
  .read-more { position: absolute; left: 18px; top: 128px; font-size: 8px; color: var(--muted); text-decoration: underline; }
  .read-more.is-active { color: var(--blue); }
  .feature-image { position: absolute; top: 152px; width: 185px; height: 67px; }

  .site-footer {
    position: absolute; left: 0; top: 918px; width: 1200px; height: 82px;
    background: var(--white); text-align: center; font-size: 11px; color: var(--muted);
  }
  .social-links { margin-top: 27px; line-height: 16px; }
  .social-links a { color: var(--muted); text-decoration: none; }
</style>
</head>
<body>
  <header class="site-header">
    <div class="brand">NORTHLINE</div>
    <nav class="main-nav">
      <a href="#" style="left:657px">Home</a>
      <a href="#" style="left:722px">About Us</a>
      <a href="#" style="left:800px">Blog</a>
      <a href="#" style="left:866px">Consulting</a>
      <a href="#" style="left:956px">Contact</a>
    </nav>
  </header>

  <h1 class="hero-title">Join My New Business <em>Bootcamp</em> for Free!</h1>
  <p class="hero-sub">Lorem Ipsum is simply dummy text of the printing and typesetting industry.</p>

  <div class="portrait" role="img" aria-label="Portrait photo of a smiling consultant in a grey suit with arms crossed"></div>

  <ul class="benefits">
    <li><svg viewBox="0 0 14 12"><path d="M1 6.5 L5 10 L13 2" fill="none" stroke="#f04a50" stroke-width="3"/></svg>Lorem Ipsum is simply dummy text of the printing and typesetting</li>
    <li><svg viewBox="0 0 14 12"><path d="M1 6.5 L5 10 L13 2" fill="none" stroke="#f04a50" stroke-width="3"/></svg>Lorem Ipsum is simply dummy text</li>
    <li><svg viewBox="0 0 14 12"><path d="M1 6.5 L5 10 L13 2" fill="none" stroke="#f04a50" stroke-width="3"/></svg>Lorem Ipsum is simply dummy text of the printing</li>
    <li><svg viewBox="0 0 14 12"><path d="M1 6.5 L5 10 L13 2" fill="none" stroke="#f04a50" stroke-width="3"/></svg>Lorem Ipsum is simply dummy text of the printing&nbsp; typesetting</li>
    <li><svg viewBox="0 0 14 12"><path d="M1 6.5 L5 10 L13 2" fill="none" stroke="#f04a50" stroke-width="3"/></svg>Lorem Ipsum is simply dummy text&nbsp; and typesetting</li>
  </ul>

  <section class="cta-bar">
    <h2 class="cta-title">Lorem Ipsum is simply dummy text of the printing and typesetting industry.</h2>
    <p class="cta-text">Lorem Ipsum is simply dummy text of the printing and typesetting industry. Lorem Ipsum has been the industry's standard dummy text ever since</p>
    <div class="cta-divider"></div>
    <a href="#" class="cta-button">Call to Action</a>
  </section>

  <section class="features">
    <article class="feature" style="left:22px">
      <div class="feature-head">THE BLOG</div>
      <p class="feature-text">Lorem Ipsum is simply dummy text of the printing and typesetting industry. Lorem Ipsum has been the industry</p>
      <a href="#" class="read-more is-active">READ MORE</a>
      <div class="feature-image" style="left:17px;background:linear-gradient(90deg,#2a1a2a,#4a3040 50%,#8a7a60)" role="img" aria-label="Photo of two people wearing sunglasses"></div>
    </article>
    <article class="feature" style="left:269px;width:224px">
      <div class="feature-head">THE BOOK</div>
      <p class="feature-text" style="left:11px">Lorem Ipsum is simply dummy text of the printing and typesetting industry. Lorem Ipsum has been the industry</p>
      <a href="#" class="read-more" style="left:11px">READ MORE</a>
      <div class="feature-image" style="left:14px;width:193px;background:linear-gradient(180deg,#8a7a6a,#c8bfb5 50%,#6a625a)" role="img" aria-label="Photo of a spiral notebook with pens"></div>
    </article>
    <article class="feature" style="left:513px;width:224px">
      <div class="feature-head">THE PODCAST</div>
      <p class="feature-text" style="left:21px">Lorem Ipsum is simply dummy text of the printing and typesetting industry. Lorem Ipsum has been the industry</p>
      <a href="#" class="read-more" style="left:21px;top:133px">READ MORE</a>
      <div class="feature-image" style="left:19px;width:189px;background:linear-gradient(90deg,#7a5a40,#c8a080 45%,#e8e0d8 70%,#5a3a2a)" role="img" aria-label="Photo of a woman listening to audio"></div>
    </article>
  </section>

  <footer class="site-footer">
    <p class="social-links"><a href="#">Facelink</a> &nbsp;|&nbsp; <a href="#">Chirper</a> &nbsp;|&nbsp; <a href="#">Linkwork</a></p>
    <p>Copyright © 2014 Company Name</p>
  </footer>
</body>
</html>
```